WALKING FOOD TOURISM BUSINESS. REQUEST FOR DIGITAL BROCHURE

Our business is a walking food tourism business in and around Melbourne's central city. We are needing a e-digital brochure - to be solely used as email' marketing content, not print. Therefore PDF size needs to be appropriate/suitable. Please see attached written content required for the brochure - together with our logo. For images, I am happy for designer to use our website content (www.gullyandfork.com). OR any other appropriate and creative 'foodie' or Melbourne image suitable. Many thanks:)

Target Market(s)

Premium brand travellers or local adventurous Australians.

Requirements
Must have
• Quality font and images
Nice to have
• Quality Melbourne and food images. See website - gullyandfork.com
Should not have
• Too much colour. Brand is black and white, sophisticated, premium product.

```html
<!DOCTYPE html>
<html lang="en">
<head>
<meta charset="utf-8">
<title>Gully &amp; Fork Experiences – Digital Brochure</title>
<link rel="stylesheet" href="https://fonts.googleapis.com/css2?family=Montserrat:wght@300;400;500;600;700&display=swap">
<style>
:root{
  --ink:#2e3142;
  --ink-soft:#4a4d5c;
  --paper:#ffffff;
  --stage:#e4e4e4;
  --rule:#8b8e9c;
  --muted:#5b5d68;
}
*{margin:0;padding:0;box-sizing:border-box}
html,body{width:1200px;height:858px;overflow:hidden;background:var(--stage);font-family:"Montserrat",sans-serif;color:var(--ink)}
.page{position:absolute;top:74px;width:503px;height:707px;background:var(--paper);overflow:hidden}
.page--front{left:84px}
.page--back{left:623px}

/* hero photos */
.hero{position:absolute;left:0;top:0;width:503px}
.hero--river{height:262px;background:linear-gradient(180deg,#5d7ea6 0%,#8aa3bf 30%,#3f5a57 60%,#2f4a5c 100%)}
.hero--lane{height:250px;background:linear-gradient(160deg,#4f4a48 0%,#7d716a 35%,#5d6770 65%,#3b3f45 100%)}
.hero-curve{position:absolute;left:0;width:503px}
.page--front .hero-curve{top:204px;height:60px}
.page--back .hero-curve{top:196px;height:60px}

/* front left column */
.brand{position:absolute;left:17px;top:318px;width:250px;text-align:center}
.brand-mark{display:inline-flex;align-items:center;gap:10px;font-size:30px;font-weight:500;color:var(--ink);letter-spacing:.5px}
.brand-dot{width:16px;height:16px;border-radius:50%;background:var(--ink)}
.brand-rule{width:220px;height:2px;background:var(--ink);margin:10px auto 0}
.intro-title{position:absolute;left:17px;top:432px;font-size:14.2px;font-weight:400;letter-spacing:.1px}
.intro-copy{position:absolute;left:17px;top:458px;width:240px;font-size:8.2px;line-height:11.6px;color:var(--muted);text-align:justify}
.intro-copy p+p{margin-top:11px}

/* front dark panel */
.panel{position:absolute;left:276px;top:258px;width:227px;height:415px;background:var(--ink);color:#fff;z-index:2}
.panel-title{position:absolute;left:0;width:227px;text-align:center;font-size:12px;font-weight:400}
.panel-title--booking{top:60px}
.panel-title--cancel{top:172px}
.panel-rule{position:absolute;left:24px;width:180px;height:1px;background:var(--rule)}
.panel-rule--a{top:83px}
.panel-rule--b{top:195px}
.phone-pill{position:absolute;left:26px;top:102px;width:173px;height:19px;border-radius:10px;background:#fff;color:var(--ink);display:flex;align-items:center;justify-content:center;gap:6px;font-size:11px;font-weight:600;letter-spacing:.8px}
.socials{position:absolute;left:26px;top:131px;width:180px;display:flex;justify-content:space-between;font-size:7.6px}
.social{display:flex;align-items:center;gap:4px}
.social-dot{width:10px;height:10px;border-radius:50%;background:#fff}
.policy{position:absolute;left:18px;width:200px;font-size:7.6px;line-height:11.4px;padding-left:8px}
.policy::before{content:"";position:absolute;left:0;top:4px;width:3px;height:3px;border-radius:50%;background:#fff}
.policy--a{top:219px}
.policy--b{top:254px}

/* front photo strip */
.thumb{position:absolute;top:563px;width:151px;height:98px;border-radius:4px;z-index:3}
.thumb--dish{left:17px;background:radial-gradient(circle at 50% 55%,#e9c16a 0%,#d9b27c 30%,#efe7dc 55%,#6f655c 100%)}
.thumb--table{left:178px;background:linear-gradient(180deg,#6a4b3e 0%,#8c6a5a 45%,#4b3a35 100%)}
.thumb--pasta{left:337px;background:radial-gradient(circle at 50% 55%,#e8d7a3 0%,#c9b07a 30%,#f3efe6 55%,#7d8c5c 100%)}

/* footer */
.footer{position:absolute;left:0;top:673px;width:503px;height:28px;background:var(--ink);color:#fff;font-size:9px;letter-spacing:.3px;display:flex;align-items:center;justify-content:space-between;padding:0 18px 0 22px;z-index:3}
.footer-item{display:flex;align-items:center;gap:6px}
.footer-item svg{width:9px;height:9px}

/* back */
.tasting{position:absolute;border-radius:50%;border:3px solid #fff;box-shadow:0 1px 3px rgba(0,0,0,.25);z-index:2}
.tasting--bar{left:113px;top:215px;width:100px;height:100px;background:radial-gradient(circle,#c9a26b 0%,#8a6a45 100%)}
.tasting--plate{left:194px;top:204px;width:114px;height:114px;background:radial-gradient(circle,#6f7d48 0%,#e7e3dc 45%,#5c5f66 100%);z-index:3}
.tasting--share{left:293px;top:215px;width:100px;height:100px;background:radial-gradient(circle,#e09a60 0%,#b5643a 55%,#6d3b24 100%)}
.tours-title{position:absolute;left:0;top:327px;width:503px;text-align:center;font-size:19px;font-weight:400;letter-spacing:.1px}
.tour{position:absolute;width:222px}
.tour--foodies{left:23px;top:360px}
.tour--street{left:23px;top:449px}
.tour--story{left:23px;top:562px}
.tour--evening{left:266px;top:360px}
.tour--private{left:266px;top:461px}
.tour-label{display:inline-block;background:var(--ink);color:#fff;font-size:6.6px;font-weight:600;padding:1px 18px 1px 2px;height:11px;line-height:9px;clip-path:polygon(0 0,100% 0,calc(100% - 9px) 100%,0 100%)}
.tour-line{border-top:1px solid var(--ink);margin-top:-1px}
.tour-meta{font-size:6.6px;font-weight:700;margin-top:2px}
.tour-copy{font-size:6px;line-height:8.4px;color:var(--muted);text-align:justify;margin-top:2px}
.tour-copy p+p{margin-top:8px}
.tour-copy strong{color:var(--ink)}
.col-divider{position:absolute;left:253px;top:368px;width:1px;height:290px;background:#d3d4d9}
</style>
</head>
<body>

<section class="page page--front">
  <div class="hero hero--river" role="img" aria-label="Photograph of the Yarra River with moored boats, a footbridge and city towers"></div>
  <svg class="hero-curve" viewBox="0 0 503 60" preserveAspectRatio="none" aria-hidden="true">
    <path d="M0 52 Q240 34 503 6 L503 60 L0 60 Z" fill="#fff"/>
    <path d="M0 50 Q240 30 503 0 L503 10 Q240 38 0 54 Z" fill="#2e3142"/>
  </svg>

  <div class="brand">
    <div class="brand-mark"><span class="brand-dot"></span>Gully &amp; Fork</div>
    <div class="brand-rule"></div>
  </div>

  <h1 class="intro-title">GULLY &amp; FORK EXPERIENCES</h1>
  <div class="intro-copy">
    <p>We provide experiential adventure for visitors and locals alike - all through the 'lens' of exceptional food.</p>
    <p>Our tour experiences capture the essence of Melbourne, its people and diverse history - stopping to sip, savour and delight in Melbourne's foodie hot spots &amp; indulging in their signature tastes.</p>
  </div>

  <aside class="panel">
    <h2 class="panel-title panel-title--booking">For Booking Schedule &amp; Enquiry</h2>
    <div class="panel-rule panel-rule--a"></div>
    <div class="phone-pill">
      <svg width="10" height="10" viewBox="0 0 24 24" aria-hidden="true"><path fill="#2e3142" d="M6.6 10.8a15 15 0 0 0 6.6 6.6l2.2-2.2a1 1 0 0 1 1-.25 11.4 11.4 0 0 0 3.6.57 1 1 0 0 1 1 1V20a1 1 0 0 1-1 1A17 17 0 0 1 3 4a1 1 0 0 1 1-1h3.5a1 1 0 0 1 1 1c0 1.25.2 2.45.57 3.57a1 1 0 0 1-.25 1Z"/></svg>
      0412 736 904
    </div>
    <div class="socials">
      <span class="social"><span class="social-dot"></span>GullyAndFork</span>
      <span class="social"><span class="social-dot"></span>gullyandfork.tours</span>
    </div>
    <h2 class="panel-title panel-title--cancel">Cancellation &amp; Amendments</h2>
    <div class="panel-rule panel-rule--b"></div>
    <p class="policy policy--a">100% REFUND for cancellations outside 24 hours of the tour departure time</p>
    <p class="policy policy--b">NO REFUND for cancellations made within 24 hours of the tour departure time</p>
  </aside>

  <div class="thumb thumb--dish" role="img" aria-label="Photograph of a plated fish dish with corn and herbs"></div>
  <div class="thumb thumb--table" role="img" aria-label="Photograph of a tour group sharing a meal at a restaurant table"></div>
  <div class="thumb thumb--pasta" role="img" aria-label="Photograph of a bowl of noodles with herbs"></div>

  <footer class="footer">
    <span class="footer-item"><svg viewBox="0 0 10 10" aria-hidden="true"><circle cx="5" cy="5" r="4.3" fill="none" stroke="#fff" stroke-width="1.2"/><rect x="2.8" y="3.6" width="4.4" height="3" fill="none" stroke="#fff" stroke-width=".8"/></svg>info@gullyandfork.com</span>
    <span class="footer-item"><svg viewBox="0 0 10 10" aria-hidden="true"><circle cx="5" cy="5" r="4.3" fill="none" stroke="#fff" stroke-width="1.2"/><path d="M3.5 3.2 L4.4 3 L5 4.3 L4.5 4.8 Q5 5.7 5.8 6 L6.3 5.5 L7.4 6.1 L7.1 7 Q5.3 7.2 3.7 5 Q3.1 4 3.5 3.2Z" fill="#fff"/></svg>0412 736 904</span>
    <span class="footer-item"><svg viewBox="0 0 10 10" aria-hidden="true"><circle cx="5" cy="5" r="4.3" fill="none" stroke="#fff" stroke-width="1.2"/><circle cx="5" cy="5" r="1.8" fill="none" stroke="#fff" stroke-width=".8"/></svg>www.gullyandfork.com</span>
  </footer>
</section>

<section class="page page--back">
  <div class="hero hero--lane" role="img" aria-label="Photograph of people walking through a cobbled laneway lined with street art"></div>
  <svg class="hero-curve" viewBox="0 0 503 60" preserveAspectRatio="none" aria-hidden="true">
    <path d="M0 46 Q250 70 503 30 L503 60 L0 60 Z" fill="#fff"/>
    <path d="M0 42 Q250 66 503 20 L503 32 Q250 72 0 48 Z" fill="#2e3142"/>
  </svg>
  <div class="tasting tasting--bar" role="img" aria-label="Photograph of a bar counter"></div>
  <div class="tasting tasting--plate" role="img" aria-label="Photograph of a plated restaurant dish"></div>
  <div class="tasting tasting--share" role="img" aria-label="Photograph of shared dumplings with sauce"></div>

  <h1 class="tours-title">GULLY &amp; FORK EXPERIENCES</h1>
  <div class="col-divider"></div>

  <article class="tour tour--foodies">
    <div class="tour-label">FOODIES BUCKET LIST TOUR</div><div class="tour-line"></div>
    <p class="tour-meta">3.5 hours / A$159 Adult / A$119 Child / Up to 8 guests</p>
    <div class="tour-copy"><p>Think you're a foodie? Are you torn by delicious culinary choices and have a fear of missing out on the true Melbourne foodie experience? If your answers are 'yes', then our 'Bucket List' adventure is for you. When time is of the essence, our 'Bucket List Tour' will 'wow' your senses - while tasting and strolling your way through Melbourne's exploding culinary epicentre.</p></div>
  </article>

  <article class="tour tour--street">
    <div class="tour-label">STREET EATS TOUR</div><div class="tour-line"></div>
    <p class="tour-meta">3.5 hours / A$159 Adult / A$119 Child / Up to 8 guests</p>
    <div class="tour-copy"><p>Hungry? Then why not broaden your palette and TAKE IT TO THE STREETS - Melbourne style. Our Street Eats Tour is ideal for locals and visitors keen to wander, explore &amp; taste Melbourne's Asian 'street food' scene. Taste your way in and around Melbourne - slurping up Thai noodles, devouring Shanghai Dumplings, Korean bites, Japanese treats and more - whilst taking in mystical immigrant stories - from the Chinese arrival, the Vietnamese and later, the sub-continent. The perfect experience to capture some of Melbourne's best, hidden treasures.</p></div>
  </article>

  <article class="tour tour--story">
    <div class="tour-label">THE STORY OF MELBOURNE</div><div class="tour-line"></div>
    <p class="tour-meta">2.5 hours / A$89 Adult / A$49 Child / Up to 12 guests</p>
    <div class="tour-copy"><p>From the Yarra River to iconic Laneways, Historic Precincts, Theatres &amp; Cathedrals - discover the character, culture &amp; community of our magnificent city, that is MELBOURNE. Walk with us on tour, as we share stories about Melbourne's past and present. Along your journey you'll take in the very fabric of Melbourne. From the early beginnings - through to today, soaking in why Melbourne continues to be one of the greatest multi-cultural cities in the world.</p></div>
  </article>

  <article class="tour tour--evening">
    <div class="tour-label">EVENING PALATE &amp; PAIRING</div><div class="tour-line"></div>
    <p class="tour-meta">3 hours / A$199 Adult / A$159 Child / Up to 8 guests</p>
    <div class="tour-copy"><p>Enjoy your evening in one of Melbourne most vibrant, mouth-watering, delectable foodie precincts. You'll be 'wowed' by Melbourne's charm and hospitality as you experience signature tastes from some of our best restaurants - pairing flavours and textures at each venue - and hearing the stories that transformed Melbourne into the marvellous 'food capital' city it is today.</p></div>
  </article>

  <article class="tour tour--private">
    <div class="tour-label">PRIVATE EXPERIENCES</div><div class="tour-line"></div>
    <p class="tour-meta">Up to 8 hours / Tailored itineraries</p>
    <div class="tour-copy">
      <p>Our private tours are ideal for the ultimate fun 'group adventure'. Share and experience the cultural delights of Melbourne with good friends - perhaps a team building event, a family reunion, a special birthday or wedding party. All with your very own personal tour host.</p>
      <p>Choose from one of our <strong>Gully &amp; Fork Experiences</strong> - with the option to customise the tour length, start time and tour distance covered. OR tailor your own experience to suit your interest, theme, community and corporate groups.</p>
      <p>Either way, your PRIVATE EXPERIENCE will be created with you in mind.</p>
      <p>Enquiries: <strong>info@gullyandfork.com</strong></p>
    </div>
  </article>

  <footer class="footer">
    <span class="footer-item"><svg viewBox="0 0 10 10" aria-hidden="true"><circle cx="5" cy="5" r="4.3" fill="none" stroke="#fff" stroke-width="1.2"/><rect x="2.8" y="3.6" width="4.4" height="3" fill="none" stroke="#fff" stroke-width=".8"/></svg>info@gullyandfork.com</span>
    <span class="footer-item"><svg viewBox="0 0 10 10" aria-hidden="true"><circle cx="5" cy="5" r="4.3" fill="none" stroke="#fff" stroke-width="1.2"/><path d="M3.5 3.2 L4.4 3 L5 4.3 L4.5 4.8 Q5 5.7 5.8 6 L6.3 5.5 L7.4 6.1 L7.1 7 Q5.3 7.2 3.7 5 Q3.1 4 3.5 3.2Z" fill="#fff"/></svg>0412 736 904</span>
    <span class="footer-item"><svg viewBox="0 0 10 10" aria-hidden="true"><circle cx="5" cy="5" r="4.3" fill="none" stroke="#fff" stroke-width="1.2"/><circle cx="5" cy="5" r="1.8" fill="none" stroke="#fff" stroke-width=".8"/></svg>www.gullyandfork.com</span>
  </footer>
</section>

</body>
</html>
```